Educational clinic needs a new webpage design

I have a relatively new website but I am unhappy with the design. I was hoping the look of it would more match my logo, brochures, business cards, and postcards. The content is good and it's already mobile ready. The designer used square space, which I would like to keep if possible. My website is www.harborlightstudyhouse.example

Target Market(s)

Parents of school age children

Industry/Entity Type

Education

Number of Pages Required

5+ page

Requirements
Must have
• Pictures must depict the diversity of our students. We service all ages, from preschool through college and our students come from varying races.
Should not have
• I try to avoid the word "tutoring" because what we do is so much more. I like the tag line of "results that go beyond traditional tutoring"

```html
<!DOCTYPE html>
<html lang="en">
<head>
<meta charset="utf-8">
<title>Harbor Light Study House</title>
<link href="https://fonts.googleapis.com/css2?family=Jost:wght@400;500&family=Arimo:wght@400;700&display=swap" rel="stylesheet">
<style>
  :root {
    --nav-green: #7cc576;
    --nav-active: #9ed47a;
    --header-green-a: #8acd75;
    --header-green-b: #aad672;
    --header-stripe: #a9d96a;
    --brand-purple: #6a2a8c;
    --heading-dark: #222222;
    --body-grey: #555555;
    --footer-grey: #bfbfbf;
    --footer-text: #5a5a5a;
    --footer-rule: #8c8c8c;
    --subscribe-purple: #9a6cc6;
    --subscribe-text: #cdb6e4;
    --social-blue: #3b5a9a;
    --white: #ffffff;
  }
  * { margin: 0; padding: 0; box-sizing: border-box; }
  html, body { width: 1200px; height: 1000px; overflow: hidden; background: var(--white); }
  .page { position: relative; width: 1200px; height: 1000px; font-family: "Arimo", Arial, sans-serif; }

  .site-nav { position: absolute; top: 0; left: 0; width: 1200px; height: 48px; background: var(--nav-green); }
  .site-nav a {
    position: absolute; top: 0; height: 48px; line-height: 48px; text-align: center;
    font-family: "Jost", "Futura", sans-serif; font-size: 20px; color: var(--white);
    text-decoration: none; letter-spacing: 0.2px;
  }
  .site-nav a.is-active, .site-nav a.nav-contact { background: var(--nav-active); }

  .site-header {
    position: absolute; top: 48px; left: 0; width: 1200px; height: 192px;
    background: linear-gradient(90deg, var(--header-green-a), var(--header-green-b) 50%, var(--header-green-a));
  }
  .header-stripe { position: absolute; top: 240px; left: 0; width: 1200px; height: 6px; background: var(--header-stripe); }

  .brand { position: absolute; top: 48px; left: 0; width: 1200px; height: 192px; display: flex; align-items: center; justify-content: center; gap: 22px; }
  .brand-mark { width: 70px; height: 70px; border-radius: 50%; background: var(--brand-purple); }
  .brand-name { font-family: "Arimo", Arial, sans-serif; font-weight: 700; font-size: 28px; color: var(--brand-purple); }

  .intro { position: absolute; top: 316px; left: 0; width: 1200px; text-align: center; }
  .intro h1 { font-size: 18px; font-weight: 700; color: var(--heading-dark); line-height: 24px; }
  .intro p { margin-top: 16px; font-size: 14.5px; line-height: 18px; color: var(--body-grey); }

  .feature { position: absolute; top: 462px; width: 338px; text-align: center; }
  .feature-about { left: 148px; }
  .feature-contact { left: 727px; }
  .feature-photo { width: 338px; height: 220px; }
  .photo-reading { background: linear-gradient(120deg, #5c6166 0%, #3a3f44 40%, #a9aeb2 70%, #c7c4bc 100%); }
  .photo-writing { background: linear-gradient(160deg, #b23a62 0%, #8a8572 20%, #b9b49a 60%, #9fa08c 100%); }
  .feature h2 { margin-top: 30px; font-size: 19px; font-weight: 700; color: var(--brand-purple); line-height: 24px; }
  .feature p { margin: 10px auto 0; width: 310px; font-size: 14.5px; line-height: 18px; color: var(--body-grey); }
  .feature .more { display: inline-block; margin-top: 8px; font-size: 14.5px; color: var(--brand-purple); text-decoration: none; }

  .site-footer { position: absolute; top: 872px; left: 0; width: 1200px; height: 128px; background: var(--footer-grey); }
  .footer-blurb { position: absolute; top: 7px; left: 0; width: 1200px; text-align: center; font-size: 14.5px; line-height: 18px; color: var(--footer-text); }
  .footer-rule { position: absolute; top: 67px; left: 201px; width: 798px; height: 1px; background: var(--footer-rule); }
  .footer-address { position: absolute; top: 78px; left: 0; width: 1200px; text-align: center; font-size: 14.5px; line-height: 18px; color: #666666; text-transform: uppercase; }
  .subscribe {
    position: absolute; top: 24px; left: 0; width: 138px; height: 29px;
    background: var(--subscribe-purple); border-radius: 0 5px 5px 0;
    font-weight: 700; font-size: 18px; line-height: 29px; padding-left: 9px; color: var(--subscribe-text);
  }
  .social-square { position: absolute; top: 24px; left: 1172px; width: 28px; height: 29px; background: var(--social-blue); border-radius: 4px 0 0 4px; }
</style>
</head>
<body>
<div class="page">
  <nav class="site-nav">
    <a class="is-active" href="#" style="left:139px;width:78px;">HOME</a>
    <a href="#" style="left:250px;width:118px;">SERVICES</a>
    <a href="#" style="left:400px;width:118px;">ABOUT US</a>
    <a href="#" style="left:552px;width:125px;">PAYMENTS</a>
    <a class="nav-contact" href="#" style="left:994px;width:154px;">CONTACT US</a>
  </nav>

  <header class="site-header"></header>
  <div class="header-stripe"></div>
  <div class="brand">
    <span class="brand-mark"></span>
    <span class="brand-name">Harbor Light Study House</span>
  </div>

  <section class="intro">
    <h1>Lorem ipsum dolor sit amet, consectetur adipiscing elit.</h1>
    <p>Aliquam rutrum turpis in nisl egestas congue eget at nunc.<br>
    Aenean viverra pellentesque eros non aliquet. Vivamus gravida,<br>
    mauris non hendrerit scelerisque, sem dolor suscipit nisi,<br>
    rhoncus accumsan erat arcu in mauris. Aenean ac tincidunt sem.</p>
  </section>

  <article class="feature feature-about">
    <div class="feature-photo photo-reading" role="img" aria-label="Student reading an illustrated book"></div>
    <h2>ABOUT</h2>
    <p>Duis lacinia, felis sed aliquet porttitor, neque eros condimentum lectus, ut feugiat sem elit sit amet arcu.</p>
    <a class="more" href="#">Read More &#8594;</a>
  </article>

  <article class="feature feature-contact">
    <div class="feature-photo photo-writing" role="img" aria-label="Child practising handwriting on a worksheet"></div>
    <h2>CONTACT US</h2>
    <p>Morbi eu porta turpis. Nam feugiat sem ut semper maximus. Praesent vehicula, mi ut tempus eleifend, dolor metus cursus erat,.</p>
    <a class="more" href="#">Find Out How &#8594;</a>
  </article>

  <footer class="site-footer">
    <div class="subscribe">SUBSCRIBE</div>
    <div class="social-square" aria-label="Social page"></div>
    <p class="footer-blurb">Aenean viverra pellentesque eros non aliquet. Vivamus gravida,<br>
    mauris non hendrerit scelerisque, sem dolor suscipit nisi,<br>
    rhoncus accumsan erat arcu in mauris. Aenean ac tincidunt sem.</p>
    <div class="footer-rule"></div>
    <p class="footer-address">Harbor Light Study House, 418 Lantern Avenue, Bayview, IL,<br>
    60900555-014-2290info@harborlightstudyhouse.example</p>
  </footer>
</div>
</body>
</html>
```